Premium Personal Brand — Facebook Banner (Used Across All Platforms)

Update — Additional Color Direction
In addition to the dark charcoal/slate direction already described, I'm also interested in seeing variants with:
Dark navy blue — Deep, authoritative, intelligence-community feel. Same textured/matte treatment, not flat or bright.
Warm charcoal with steel blue accent — Keep the dark base but introduce a subtle steel blue gradient, accent line, or tonal shift. Sophisticated, modern, adds dimension without adding color noise.
Both should maintain the same premium, restrained, architectural feel described in the original brief. No bright blues, no corporate PowerPoint energy — think midnight, think depth, think weight.
Everything else in the brief remains the same.
I am building a premium personal brand as an executive advisor to founders ($5M+ revenue).
This contest is Facebook-banner–focused, but the design must represent a visual system that will be reused across:
- LinkedIn
- YouTube
I- nstagram
- X (Twitter)
- Website hero sections and other brand touchpoints
Think of the Facebook banner as the primary expression of the brand — not a one-off graphic.
This project is about discovering a high-end visual style and brand feel, not decoration.
What to design
Please submit one cohesive visual system, shown primarily as:
- Facebook banner (primary focus)
The same design language should clearly translate to all platforms listed above.
Designers are responsible for using the current recommended dimensions for each platform.
Quick clarification on background direction:
Backgrounds should have depth and texture, not flat color fields. Avoid pure white, light grey, or solid black backgrounds. Think matte, architectural materials — stone, graphite, concrete, steel — not blank canvases. Subtle tonal variation is encouraged. Obvious gradients or decorative patterns are not.
Text to use
Primary Headline:
- Your Business Is Too Valuable To Be Run On Hope.
Subheadline:
- You didn’t build a business to become its prisoner.
Name:
Paul Whitaker
The headline should be the dominant visual element.
Logo note (important)
My personal logo is currently being finalized.
For this contest:
- Use a simple “PW” monogram placeholder
- Clean, bold, geometric sans-serif
- Do not design a logo
- The winning design must allow an easy logo swap later.
Headshot note (important)
- Please do not include a headshot in the banner design.
- Most platforms display a circular profile image separately.
- The banner should stand on its own using typography, layout, and tone only.
- Design the banner assuming the profile photo will sit nearby, not inside the banner.
Style direction
The design should feel:
- Premium
- Calm
- Confident
- Restrained
- High-trust
- Dark, neutral backgrounds are preferred.
- Fewer elements are better than more.
Think:
- Owner-level advisor
- Private equity / boardroom tone
- Industrial, Modern, Minimalist, Elite, Architectural, not decorative
What to avoid
Please do not submit designs that feel:
- Promotional, hype-driven, or salesy
- Like a coach, guru, or agency
- Bright, colorful, or gradient-heavy
- Busy or over-designed
- Based on stock photos
- No motivational speaker energy.
Reaction test
- If someone sees this banner on Facebook (or later on LinkedIn, YouTube, etc.), the reaction should be:
“That person is serious. I’d trust them with important decisions.”
Final note
- I am not looking for many variations.
- I am looking for one strong visual direction you believe in.
Simple beats clever.
- Restraint beats decoration.

```html
<!DOCTYPE html>
<html lang="en">
<head>
<meta charset="UTF-8">
<title>Paul Whitaker — Cover Banner</title>
<link rel="stylesheet" href="https://fonts.googleapis.com/css2?family=Jost:wght@300;400;600;700&display=swap">
<style>
  :root {
    --stage: #9a9a9a;
    --navy: #021630;
    --navy-tone: #0a1f3b;
    --monogram-faint: #1b2c46;
    --white: #ffffff;
    --green-deep: #0b8a43;
    --green-light: #7bbf4e;
  }
  * { margin: 0; padding: 0; box-sizing: border-box; }
  html, body {
    width: 1200px;
    height: 900px;
    overflow: hidden;
    background: var(--stage);
    font-family: "Jost", sans-serif;
  }
  .canvas {
    position: relative;
    width: 1200px;
    height: 900px;
  }
  .cover {
    position: absolute;
    left: 0;
    top: 228px;
    width: 1200px;
    height: 444px;
    overflow: hidden;
    background: radial-gradient(ellipse at 70% 50%, var(--navy-tone) 0%, var(--navy) 70%);
    color: var(--white);
  }
  .cover__backdrop-mark {
    position: absolute;
    right: -30px;
    top: -150px;
    font-weight: 700;
    font-size: 640px;
    line-height: 1;
    letter-spacing: -20px;
    color: var(--monogram-faint);
    user-select: none;
  }
  .cover__monogram {
    position: absolute;
    left: 0;
    right: 0;
    top: 40px;
    text-align: center;
    font-weight: 600;
    font-size: 112px;
    line-height: 1;
    letter-spacing: -2px;
    color: var(--white);
  }
  .cover__headline {
    position: absolute;
    left: 0;
    right: 0;
    top: 166px;
    text-align: center;
    font-weight: 400;
    font-size: 62px;
    line-height: 73px;
    letter-spacing: -0.5px;
  }
  .cover__headline .accent-deep { color: var(--green-deep); font-weight: 600; }
  .cover__headline .accent-light { color: var(--green-light); font-weight: 600; }
  .cover__subline {
    position: absolute;
    left: 169px;
    top: 320px;
    width: 861px;
    height: 51px;
    border-radius: 26px;
    background: var(--green-deep);
    display: flex;
    align-items: center;
    justify-content: center;
    font-weight: 300;
    font-size: 33px;
    color: var(--white);
    letter-spacing: 0.2px;
  }
</style>
</head>
<body>
  <main class="canvas">
    <section class="cover" aria-label="Paul Whitaker cover banner">
      <div class="cover__backdrop-mark" aria-hidden="true">PW</div>
      <div class="cover__monogram" aria-label="Paul Whitaker">PW</div>
      <h1 class="cover__headline">
        Your Business Is Too <span class="accent-deep">Valuable</span><br>
        To Be <span class="accent-light">Run</span> On <span class="accent-light">Hope</span>
      </h1>
      <p class="cover__subline">You didn’t build a business to become its prisoner</p>
    </section>
  </main>
</body>
</html>
```